Banner Ad Design Project

We need a 728x90 and a 300x250
1st option
"I have a lead for you. Click here to close the deal."
In large bold letters.
Under this in smaller letters,
"Borwelt. For serious business networkers"
2nd option
"Put that coffee down!"
"Coffee's for closers only."
Close more deals. BORWELT LOGO
(this is a quote from Harrowmere Tavish. It is a famous sales movie)
The other option is
"First you get the money" "Then you get the power" in bold letters.
"Borwelt. For serious business networkers" in smaller letters at the bottom.
-Must have our colors
-Must have our logo (Small at the bottom right)
-Watch the video at borwelt () com
Please be creative. If the banner can have multiple images that would be great as well.
This needs to be a serious looking ad that is bold and clean.
Updates
Please be sure to use the phrase, "Put that coffee down! Coffee's for closers only" with the logo and at the bottom the words, Borwelt, for serious business networkers. in one of the designs. This will be our first campaign. I am looking for a very simple design that is bold. Perhaps just a coffee cup with the words and no other graphics.
Target Market(s)
Sales professionals
Industry/Entity Type
Business
Look and feel

```html
<!DOCTYPE html>
<html lang="en">
<head>
<meta charset="utf-8">
<title>Borwelt banner ads – coffee's for closers</title>
<link rel="stylesheet" href="https://fonts.googleapis.com/css2?family=Ubuntu:wght@700&family=Arimo:wght@400&display=swap">
<style>
  :root {
    --backdrop: #6a4427;
    --panel: #ffffff;
    --headline: #f0a113;
    --tagline: #2f4c96;
    --accent-green: #7cb342;
    --accent-blue: #4a5ea6;
    --accent-blue-light: #8fa0d6;
  }
  * { box-sizing: border-box; margin: 0; padding: 0; }
  html, body {
    width: 1200px;
    height: 676px;
    overflow: hidden;
    background: var(--backdrop);
  }
  .canvas {
    position: relative;
    width: 1200px;
    height: 676px;
  }
  .banner {
    position: absolute;
    background: var(--panel);
    border-top: 5px solid var(--accent-green);
    box-shadow: 0 6px 14px rgba(0, 0, 0, 0.45);
    text-align: center;
  }
  .banner::after {
    content: "";
    position: absolute;
    left: 0; right: 0; bottom: 0;
    height: 10px;
    background: var(--accent-blue);
    border-top: 2px solid var(--accent-blue-light);
  }
  .headline {
    font-family: "Ubuntu", sans-serif;
    font-weight: 700;
    color: var(--headline);
  }
  .tagline {
    font-family: "Arimo", Arial, sans-serif;
    font-weight: 400;
    color: var(--tagline);
  }
  .brand {
    font-family: "Ubuntu", sans-serif;
    font-weight: 700;
    color: var(--headline);
    display: inline-flex;
    align-items: center;
    gap: 6px;
  }
  .brand-mark {
    display: inline-block;
    border-radius: 50%;
    background: var(--headline);
  }

  /* 728x90 leaderboard */
  .banner--leaderboard {
    left: 78px;
    top: 65px;
    width: 1044px;
    height: 128px;
  }
  .banner--leaderboard .headline {
    position: absolute;
    left: 0; right: 0;
    top: 16px;
    font-size: 38px;
    line-height: 44px;
  }
  .banner--leaderboard .tagline {
    position: absolute;
    left: 0; right: 0;
    top: 75px;
    font-size: 21px;
    line-height: 24px;
  }
  .banner--leaderboard .brand {
    position: absolute;
    right: 8px;
    bottom: 14px;
    font-size: 15px;
  }
  .banner--leaderboard .brand-mark { width: 12px; height: 12px; }

  /* 300x250 medium rectangle */
  .banner--rectangle {
    left: 385px;
    top: 253px;
    width: 430px;
    height: 361px;
  }
  .banner--rectangle .headline {
    position: absolute;
    left: 0; right: 0;
    top: 5px;
    font-size: 49px;
    line-height: 59px;
  }
  .banner--rectangle .brand {
    position: absolute;
    left: 0; right: 0;
    top: 258px;
    justify-content: center;
    font-size: 34px;
    line-height: 40px;
  }
  .banner--rectangle .brand-mark { width: 26px; height: 26px; }
  .banner--rectangle .tagline {
    position: absolute;
    left: 0; right: 0;
    top: 318px;
    font-size: 21px;
    line-height: 24px;
  }
</style>
</head>
<body>
<main class="canvas">
  <section class="banner banner--leaderboard" aria-label="728 by 90 banner">
    <h1 class="headline">Put that coffee down! Coffee's for closers only.</h1>
    <p class="tagline">Borwelt. For serious business networkers.</p>
    <span class="brand"><span class="brand-mark"></span>Borwelt</span>
  </section>

  <section class="banner banner--rectangle" aria-label="300 by 250 banner">
    <h2 class="headline">Put that<br>coffee down!<br>Coffee's for<br>closers only.</h2>
    <span class="brand"><span class="brand-mark"></span>Borwelt</span>
    <p class="tagline">For serious business networkers.</p>
  </section>
</main>
</body>
</html>
```